Sticker label for natural moisturizer

I need a sticker label designed for a homemade moisturizer made from beef tallow and honey.
Must include: Logo, product name (Classic Suet & Clover Salve), ingredients (in English and Polish, can use placeholder text for initial design), brief description of product with instructions for use (in English and Polish, can use placeholder text for initial design), manufacturer name (vorelmart.com), manufacturer address (placeholder text for initial design), volume of container (60ml / 2oz)
The product is used by both males and females of all ages, so must be unisex design with broad appeal.
Dimensions: Length 15cm, Height 3cm
Style: Has to simultaneously communicate that this is a homemade product with no chemical fillers AND that it is of extremely high quality.
Brand colors:
#57665C
#FCFAF6
#FFFFFF
#000000
#B99B83
#EAE4DD
#CC8E5A

```html
<!DOCTYPE html>
<html lang="en">
<head>
<meta charset="utf-8">
<title>Classic Suet &amp; Clover Salve – Jar Label</title>
<link rel="stylesheet" href="https://fonts.googleapis.com/css2?family=Roboto+Condensed:wght@400;700&family=Jost:wght@400&family=Lora:wght@600&display=swap">
<style>
  :root {
    --backdrop: #d9dccb;
    --cream: #faf1e8;
    --sage: #536358;
    --forest: #2d3731;
    --ink: #1f2a24;
    --text-muted: #55605a;
    --white: #ffffff;
    --white-soft: #e8ece6;
    --illustration-a: #dfe6dc;
    --illustration-b: #f3efe6;
  }
  * { box-sizing: border-box; margin: 0; padding: 0; }
  html, body { width: 1200px; height: 1062px; overflow: hidden; }
  body { background: var(--backdrop); position: relative; }

  .label {
    position: absolute;
    left: 86px; top: 426px;
    width: 1028px; height: 209px;
    overflow: hidden;
  }
  .band { position: absolute; left: 0; width: 100%; }
  .band--cream { top: 0; height: 97px; background: var(--cream); }
  .band--sage { top: 97px; height: 83px; background: var(--sage); }
  .band--forest { top: 180px; height: 29px; background: var(--forest); }

  .copy-block {
    position: absolute;
    width: 350px;
    font-family: "Roboto Condensed", sans-serif;
    font-size: 13px;
    line-height: 16.7px;
  }
  .copy-block .line {
    display: block;
    white-space: nowrap;
    text-align: justify;
    text-align-last: justify;
  }
  .copy-block .line--last { text-align-last: left; }
  .copy-block strong { font-weight: 700; }

  .copy-block--left { left: 21px; }
  .copy-block--right { left: 657px; }
  .copy-block--en { top: 31px; color: var(--text-muted); }
  .copy-block--pl { top: 98px; color: var(--white); }

  .floral-art {
    position: absolute;
    left: 428px; top: 0;
    width: 188px; height: 97px;
    background: radial-gradient(ellipse at 55% 60%, var(--illustration-a), var(--illustration-b) 75%, var(--cream));
  }
  .brand-name {
    position: absolute;
    left: 362px; width: 300px;
    top: 36px;
    text-align: center;
    font-family: "Lora", serif;
    font-weight: 600;
    font-size: 50px;
    line-height: 56px;
    color: var(--ink);
  }

  .product-name {
    position: absolute;
    left: 362px; width: 300px;
    top: 116px;
    text-align: center;
    font-family: "Jost", sans-serif;
    font-weight: 400;
    font-size: 25px;
    line-height: 25px;
    color: var(--white);
    letter-spacing: 0.3px;
  }
  .volume {
    position: absolute;
    left: 362px; width: 300px;
    top: 183px;
    text-align: center;
    font-family: "Jost", sans-serif;
    font-size: 17px;
    line-height: 22px;
    color: var(--white);
  }
  .maker {
    position: absolute;
    left: 657px; width: 350px;
    top: 180px; height: 29px;
    line-height: 29px;
    text-align: right;
    white-space: nowrap;
    font-family: "Roboto Condensed", sans-serif;
    font-size: 12px;
    color: var(--white-soft);
  }
  .maker strong { font-weight: 700; color: var(--white); }
</style>
</head>
<body>
  <section class="label" aria-label="Jar label">
    <div class="band band--cream"></div>
    <div class="band band--sage"></div>
    <div class="band band--forest"></div>

    <p class="copy-block copy-block--left copy-block--en">
      <span class="line"><strong>Ingredients:</strong> 100% Grass-fed Irish Beef Tallow (Tallow), Cold</span>
      <span class="line">Pressed Extra-virgin Olive Oil (Olea Europaea Fruit Oil), Beeswax</span>
      <span class="line">(Cera Alba), Raw Irish Honey (Mel), Essential oils of Frankincense</span>
      <span class="line line--last">Carterii (Boswellia carterii), Neroli (Citrus aurantium amara)</span>
    </p>

    <p class="copy-block copy-block--left copy-block--pl">
      <span class="line"><strong>Skladniki:</strong> 100% irlandzkiego lóju wolowego (lóju) pochodzacego</span>
      <span class="line">od zwierzat karmionych trawa, tloczona na zimno oliwa z oliwek z</span>
      <span class="line">pierwszego tloczenia (Olea Europaea Fruit Oil), wosk pszczeli</span>
      <span class="line">(Cera Alba), surowy miód irlandzki (Mel), olejki eteryczne z kadzidla</span>
      <span class="line line--last">Carterii (Boswellia carterii), Neroli (Citrus aurantium amara)</span>
    </p>

    <div class="floral-art" role="img" aria-label="Faint line illustration of a flower with a bee"></div>
    <div class="brand-name">vorel</div>

    <h1 class="product-name">CLASSIC SUET<br>&amp; CLOVER SALVE</h1>
    <p class="volume">60ml / 2oz</p>

    <p class="copy-block copy-block--right copy-block--en">
      <span class="line"><strong>About:</strong> A rich balm of grass-fed tallow and raw honey that</span>
      <span class="line">softens, soothes and protects dry skin. No fillers added.</span>
      <span class="line"><strong>How to use:</strong> Warm a little between your fingertips and</span>
      <span class="line line--last">massage into clean skin, morning and evening.</span>
    </p>

    <p class="copy-block copy-block--right copy-block--pl">
      <span class="line"><strong>Opis:</strong> Bogaty balsam z łoju wołowego i surowego miodu, który</span>
      <span class="line">zmiękcza, koi i chroni suchą skórę. Bez zbędnych dodatków.</span>
      <span class="line"><strong>Sposób użycia:</strong> Rozgrzać odrobinę w palcach i wmasować</span>
      <span class="line line--last">w czystą skórę rano i wieczorem. Do użytku zewnętrznego.</span>
    </p>

    <p class="maker"><strong>vorelmart.com</strong> · 12 Placeholder Lane, Sample Town, Country</p>
  </section>
</body>
</html>
```